Power Point Template Kalmora sustainability consulting

Please note:
We are not looking for new design proposals anymore since we've already received templetes from two designers that we really like. We are currently discussing possible changes with them and will make a final decision soon. Thank you very much.

(find english description below)
We are a small German start-up that offers sustainability consulting. For presentations of results, our company presentation, proposals, lectures, etc., we need a PowerPoint template that matches our logo. We come from classic management consulting / strategy consulting and also deal with facts and figures in sustainability consulting. Therefore, the template should not be too fancy and should not only consist of photos. But it shouldn't be a completely sober template either. Our logo with the green leaves for sustainability (three leaves for KALmora) and the white bar chart (with the dynamic swing upwards) reflects our attitude well, where we see ourselves on the range from playful to sober and classic to modern.

It might be nice for the template to include the shape of one of the leaves (from the logo). Also, the logo should appear in a corner of each slide. The colors from the logo (see appendix) should be partially reflected in the presentation. We can also imagine a gold-brown tone (see website www.kalmora-consulting.example) or a coral tone as a contrast. (Attention - the website is not final yet).

For a first suggestion, it is sufficient to suggest three to four slides (cover sheet, chapter/separation slide, text slide, data slide). We will then mark drafts that we like. In total, we would then need about 6-10 more slide templates, e.g. about us, team, slide for a statement, 2-3 data charts (pie, bar, column), top 3 - 5 list, timeline, contact (more slides are welcome ).

We are a small German start-up offering sustainability consulting. We need a power point template for result presentations, our company presentation, proposals, lectures etc. The template should be aligned with our logo. Our background lies in classic management consulting / strategy consulting and we also deal with facts and figures in sustainability consulting. Therefore, the template should not be too playful and not only consist of photos. But it should also not be a completely clear template. Our logo with the green leaves for sustainability (three leaves for KALmora) and the white bar chart (with the dynamic upward swing) reflects our attitude well, where we see ourselves on the range from playful to down-to-earth and classic to modern .

For the template, it might be nice to incorporate the shape of one of the leaves (from the logo). Also, the logo should show up in one corner on each slide. Some of the colors from the logo (see attachment) should be reflected in the presentation. We could also think of a gold-brown tone (see website www.kalmora-consulting.example) or a coral tone for contrast. (Attention - the website is not final yet).

For a first proposal it is quite sufficient to suggest us three to four slides (cover page, chapter/separation slide, text slide, data slide). We will then mark the drafts that we like. In total we would need about 6-10 more slide templates, eg About us, Team, slide for a statement, 2-3 data charts (pie, bar, column), Top 3 - 5 List, Timeline, Contact (more slides are welcome).

Target Market(s)

Corporations, large companies and SMEs

Industry/Entity Type

Unternehmensberatung, Nachhaltigkeitsberatung

Font styles to use
Sans Serif
Other font styles liked:
• Calibri

Colors
00AB8E
00BBA5
67D7C9
C6EFE9
E9F9F6

Requirements
Must have
• see description (e.g. the colors of our logo)
Nice to have
• see description (e.g. elements of the logo included)
Should not have
• see description

```html
<!DOCTYPE html>
<html lang="en">
<head>
<meta charset="utf-8">
<title>Kalmora – Slide Template Overview</title>
<link rel="stylesheet" href="https://fonts.googleapis.com/css2?family=Roboto:ital,wght@0,300;0,400;0,500;0,700;1,400&display=swap">
<style>
:root{
  --stage:#c5c5c5;
  --green:#86b53a;
  --green-soft:#a9cf55;
  --green-dark:#3f6b1e;
  --gold:#c6a24d;
  --graphite:#4d4d4d;
  --ink:#1e1e1e;
  --text:#555;
  --muted:#9a9a9a;
  --rule:#d9d9d9;
  --white:#fff;
}
*{box-sizing:border-box;margin:0;padding:0}
html,body{width:1200px;height:389px;overflow:hidden}
body{background:var(--stage);font-family:"Roboto",sans-serif;position:relative;color:var(--text)}
.slide{position:absolute;width:260px;height:146px;background:var(--white);overflow:hidden;box-shadow:0 1px 3px rgba(0,0,0,.18)}
.abs{position:absolute}
.brand{position:absolute;left:11px;top:8px;display:flex;align-items:center;gap:2px;font-size:4.2px;color:var(--graphite);font-weight:400}
.brand i{display:block;width:3.4px;height:3.4px;border-radius:50%;background:var(--green)}
.slide-title{position:absolute;left:0;right:0;top:8px;text-align:center;font-size:13px;font-weight:700;color:var(--ink);letter-spacing:-.1px}
.footer-url{position:absolute;left:12px;bottom:9px;display:flex;align-items:center;gap:3px;font-size:2.6px;color:var(--muted)}
.footer-url i{display:block;width:5px;height:5px;border-radius:50%;border:.6px solid var(--green-soft)}
.next-arrow{position:absolute;right:12px;bottom:8px;width:6px;height:5px}
.tiny{font-size:2.6px;line-height:1.45}
/* agenda */
.agenda{background:linear-gradient(135deg,#7aa52d 0%,#4f7d22 55%,#3e4a33 100%)}
.agenda .slide-title{color:var(--white);font-weight:500;top:9px}
.agenda-item{position:absolute;width:100px}
.agenda-item .ico{position:absolute;left:-13px;top:0;width:8px;height:8px}
.agenda-item h4{font-size:5.3px;font-weight:500;color:var(--gold);margin-bottom:2px}
.agenda-item p{font-size:2.6px;line-height:1.55;color:var(--white)}
.agenda .footer-url{color:#d7e3c4}
/* list slide */
.lead{font-size:4.4px;line-height:1.35;color:#333}
.lead em{font-style:normal;color:var(--gold)}
.check{position:absolute;left:34px;width:200px;font-size:3.4px;line-height:1.5;color:#444}
.check::before{content:"";position:absolute;left:-10px;top:.5px;width:3px;height:1.6px;border-left:.7px solid var(--green);border-bottom:.7px solid var(--green);transform:rotate(-45deg)}
/* icon list */
.icon-col{position:absolute;top:53px;width:34px;text-align:center}
.icon-col .ring{width:17px;height:17px;border-radius:50%;border:.7px solid var(--graphite);margin:0 auto 4px;display:flex;align-items:center;justify-content:center}
.icon-col .ring b{display:block;width:6px;height:6px;border:.6px solid var(--gold);border-radius:50%}
.icon-col h5{font-size:3.2px;font-weight:400;color:var(--gold);margin-bottom:1px}
.icon-col p{font-size:2.2px;line-height:1.3;color:var(--muted)}
.band{position:absolute;left:18px;right:11px;top:98px;height:6.5px;background:#8a8a8a;color:var(--white);font-size:3.6px;padding:1.3px 3px;line-height:1}
/* table slide */
.table{position:absolute;left:6px;top:66px;width:192px;border-collapse:collapse}
.table th{font-size:3.8px;font-weight:400;color:var(--gold);text-align:left;padding:1px 0 2px;border-bottom:.4px solid var(--rule)}
.table td{font-size:2.7px;color:#444;padding:2.2px 0;border-bottom:.4px solid var(--rule)}
.table tr.change td{color:var(--gold);font-size:3.4px;border-bottom:.5px solid #bbb}
.stats{position:absolute;left:203px;top:38px;width:57px}
.stats .head{background:#3d3d3d;color:var(--white);font-size:3.8px;font-weight:500;padding:3.5px 6px;height:12px}
.stats .cell{background:var(--green-soft);color:var(--white);font-size:3.6px;line-height:1.3;padding:2.3px 12px;height:17.8px;border-top:.8px solid #fff}
.stats .cell b{font-weight:500;display:block}
/* chart slide */
.legend{position:absolute;top:114px;left:0;right:0;display:flex;justify-content:center;gap:26px;font-size:4px;letter-spacing:1px;color:#333}
.legend span::before{content:"";display:inline-block;width:2.6px;height:2.6px;margin-right:3px}
.legend .g::before{background:var(--green)}
.legend .o::before{background:var(--gold)}
.legend .d::before{background:var(--graphite)}
/* number slide */
.num{position:absolute;top:32px;width:28px;height:28px;color:var(--white);text-align:center}
.num strong{display:block;font-size:6.4px;font-weight:500;margin-top:6px}
.num small{font-size:2.5px}
</style>
</head>
<body>

<!-- Cover -->
<section class="slide" style="left:35px;top:33px">
  <svg class="abs" style="left:0;top:0" width="260" height="146" viewBox="0 0 260 146">
    <defs>
      <linearGradient id="forest" x1="0" y1="0" x2="0" y2="1">
        <stop offset="0" stop-color="#7c8f5a"/>
        <stop offset=".45" stop-color="#35562a"/>
        <stop offset="1" stop-color="#213a1a"/>
      </linearGradient>
    </defs>
    <path d="M100 12 C135 4 170 14 184 38 C200 62 196 90 180 112 C162 136 120 142 96 132 C70 122 62 96 70 76 C76 60 62 44 74 28 C82 18 90 14 100 12Z" fill="var(--green)"/>
    <path d="M102 17 C134 10 166 20 179 41 C193 63 190 89 175 108 C158 130 121 136 99 127 C76 118 69 96 76 77 C81 62 69 46 79 32 C86 23 93 19 102 17Z" fill="url(#forest)" role="img" aria-label="Forest photograph with sunlight through the trees"/>
    <circle cx="152" cy="15" r="7" fill="var(--green-soft)"/>
    <circle cx="169" cy="16" r="3.5" fill="var(--green)"/>
    <circle cx="153" cy="26" r="1.5" fill="var(--green)"/>
    <circle cx="70" cy="36" r="3" fill="var(--green-soft)"/>
    <circle cx="191" cy="99" r="7" fill="var(--green-dark)"/>
    <circle cx="76" cy="112" r="3.5" fill="var(--green-soft)"/>
    <circle cx="67" cy="104" r="1.5" fill="var(--green)"/>
    <circle cx="184" cy="112" r="1.5" fill="var(--green)"/>
  </svg>
  <div class="abs" style="left:80px;top:68px;width:100px;text-align:center;color:#fff">
    <div style="font-size:9.4px;font-weight:500;line-height:1.1">Environment<br>Presentation Slide</div>
    <div style="font-size:2.8px;margin-top:3px;line-height:1.3">This is <b>environment</b> powerpoint presentation<br>template</div>
  </div>
  <div class="abs" style="left:121px;top:112px;width:18px;height:5px;border-radius:3px;background:var(--gold);color:#fff;font-size:2.8px;text-align:center;line-height:5px">2023</div>
</section>

<!-- Agenda -->
<section class="slide agenda" style="left:325px;top:33px">
  <h2 class="slide-title">Content Agenda</h2>
  <div class="agenda-item" style="left:35px;top:32px"><svg class="ico" viewBox="0 0 8 8"><path d="M1 6 L4 2 L7 6Z" fill="var(--gold)"/></svg><h4>Description</h4><p>A wonderful serenity has taken possession of my entire soul, like these sweet mornings of spring which I enjoy with my whole heart.</p></div>
  <div class="agenda-item" style="left:149px;top:32px"><svg class="ico" viewBox="0 0 8 8"><circle cx="4" cy="4" r="3" fill="var(--gold)"/></svg><h4>Description</h4><p>A wonderful serenity has taken possession of my entire soul, like these sweet mornings of spring which I enjoy with my whole heart.</p></div>
  <div class="agenda-item" style="left:35px;top:65px"><svg class="ico" viewBox="0 0 8 8"><path d="M1 4 L4 1 L7 4 V7 H1Z" fill="var(--gold)"/></svg><h4>Description</h4><p>A wonderful serenity has taken possession of my entire soul, like these sweet mornings of spring which I enjoy with my whole heart.</p></div>
  <div class="agenda-item" style="left:149px;top:65px"><svg class="ico" viewBox="0 0 8 8"><rect x="1.5" y="1" width="5" height="6" rx="1" fill="var(--gold)"/></svg><h4>Description</h4><p>A wonderful serenity has taken possession of my entire soul, like these sweet mornings of spring which I enjoy with my whole heart.</p></div>
  <div class="agenda-item" style="left:35px;top:98px"><svg class="ico" viewBox="0 0 8 8"><path d="M1 7 L4 1 L7 7Z" fill="var(--gold)"/></svg><h4>Description</h4><p>A wonderful serenity has taken possession of my entire soul, like these sweet mornings of spring which I enjoy with my whole heart.</p></div>
  <div class="agenda-item" style="left:149px;top:98px"><svg class="ico" viewBox="0 0 8 8"><rect x="1" y="3" width="6" height="4" fill="var(--gold)"/></svg><h4>Description</h4><p>A wonderful serenity has taken possession of my entire soul, like these sweet mornings of spring which I enjoy with my whole heart.</p></div>
  <div class="footer-url"><i style="border-color:#d7e3c4"></i>www.kalmora-consulting.example</div>
  <svg class="next-arrow" viewBox="0 0 6 5"><path d="M0 2.5H5M3 .5L5 2.5 3 4.5" stroke="#fff" stroke-width=".7" fill="none"/></svg>
</section>

<!-- Text list -->
<section class="slide" style="left:615px;top:33px">
  <div class="brand"><i></i>Kalmora</div>
  <h2 class="slide-title">Traditional single list</h2>
  <p class="lead abs" style="left:20px;top:33px;width:222px"><em>Contrary to popular belief</em>, Lorem Ipsum is not simply random text. It has roots in a piece of classical Latin literature from 45 BC.</p>
  <div class="abs" style="left:18px;top:52px;width:222px;height:.6px;background:var(--gold)"></div>
  <p class="check" style="top:62px">Quisque libero purus, bibendum nec quam sit amet, porta interdum ex. Aliquam erat volutpat. Quisque commodo lacus sed lectus condimentum cursus.</p>
  <p class="check" style="top:76px">Praesent a diam neque. Aenean ultricies eu orci id euismod. Integer eleifend, lacus quis tincidunt posuere, nisl neque sodales justo, quis suscipit libero odio ut quam.</p>
  <p class="check" style="top:90px">Nam auctor, leo a volutpat rhoncus, erat arcu dignissim velit, in aliquet erat metus quis tellus. Vestibulum nec lobortis augue, at interdum nisl.</p>
  <p class="abs" style="left:25px;top:108px;width:216px;font-size:4px;line-height:1.7;color:#444">Cras laoreet mauris eget pharetra auctor. Donec lacinia est id euismod eleifend. Quisque condimentum varius ullamcorper. Nunc quam libero, feugiat ut ante eu, ultrices efficitur erat.</p>
  <div class="footer-url"><i></i>www.kalmora-consulting.example</div>
  <svg class="next-arrow" viewBox="0 0 6 5"><path d="M0 2.5H5M3 .5L5 2.5 3 4.5" stroke="var(--green)" stroke-width=".7" fill="none"/></svg>
</section>

<!-- Icon list -->
<section class="slide" style="left:905px;top:33px">
  <div class="brand"><i></i>Kalmora</div>
  <h2 class="slide-title">Icon List Concept</h2>
  <p class="abs" style="left:20px;top:36px;width:222px;font-size:3px;line-height:1.5;color:#666;text-align:justify"><b style="color:var(--gold);font-weight:500">Lorem ipsum dolor sit amet, consectetur adipiscing elit.</b> Through our high performance, low CO2 concrete mixes and certified sustainability specialists, we continue to contribute to the building of projects that are environmentally responsible, cost-effective and healthy places to live and work.</p>
  <div class="icon-col" style="left:19px"><div class="ring"><b></b></div><h5>CO2 emission</h5><p>Lorem ipsum dolor sit amet, consectetur adis piscing ult adis pis</p></div>
  <div class="icon-col" style="left:57px"><div class="ring"><b></b></div><h5>Recyclable</h5><p>Lorem ipsum dolor sit amet, consectetur adis piscing ult adis pis</p></div>
  <div class="icon-col" style="left:96px"><div class="ring"><b></b></div><h5>Cost benefits</h5><p>Lorem ipsum dolor sit amet, consectetur adis piscing ult adis pis</p></div>
  <div class="icon-col" style="left:135px"><div class="ring"><b></b></div><h5>Reduces storm</h5><p>Lorem ipsum dolor sit amet, consectetur adis piscing ult adis pis</p></div>
  <div class="icon-col" style="left:174px"><div class="ring"><b></b></div><h5>Energy efficient</h5><p>Lorem ipsum dolor sit amet, consectetur adis piscing ult adis pis</p></div
  ><div class="icon-col" style="left:213px"><div class="ring"><b></b></div><h5>Durability</h5><p>Lorem ipsum dolor sit amet, consectetur adis piscing ult adis pis</p></div>
  <div class="band">CONCRETE IS THE FUTURE OF SUSTAINABLE CONSTRUCTION</div>
  <p class="abs" style="left:18px;top:108px;width:231px;font-size:3.1px;line-height:1.4;color:#777;text-align:justify">Increasingly, concrete is being recognized for its life cycle environmental and economical benefits, from extraction and production, to construction, maintenance and disposal. There are solid facts that make concrete the right choice for effective sustainable development.</p>
  <div class="footer-url"><i></i>www.kalmora-consulting.example</div>
  <svg class="next-arrow" viewBox="0 0 6 5"><path d="M0 2.5H5M3 .5L5 2.5 3 4.5" stroke="var(--green)" stroke-width=".7" fill="none"/></svg>
</section>

<!-- Section break -->
<section class="slide" style="left:35px;top:209px;background:linear-gradient(135deg,#d9d9d7,#c9c9c6)" role="img" aria-label="Light concrete texture background">
  <div class="abs" style="left:20px;top:25px;width:55px;height:115px;border-radius:40%;background:radial-gradient(ellipse at center,#6a9a2c 0%,#8fbf45 45%,rgba(200,200,196,0) 72%)" role="img" aria-label="Green leaves arranged in the shape of footprints"></div>
  <svg class="abs" style="left:0;top:0" width="260" height="146" viewBox="0 0 260 146">
    <path d="M112 16 C150 8 196 14 210 46 C224 78 212 114 186 130 C160 146 118 140 100 122 C82 104 92 84 90 66 C88 46 86 22 112 16Z" fill="#a6a6a6"/>
    <circle cx="151" cy="15" r="7" fill="#8c8c8c"/>
    <circle cx="168" cy="15" r="3" fill="#8c8c8c"/>
    <circle cx="161" cy="26" r="1.4" fill="#8c8c8c"/>
    <circle cx="191" cy="99" r="7" fill="#a0a0a0"/>
    <circle cx="75" cy="112" r="3" fill="#a0a0a0"/>
    <path d="M120 56 H136 V60 C136 65 132 68 128 68 C124 68 120 65 120 60Z" fill="none" stroke="var(--gold)" stroke-width="1.3"/>
    <path d="M136 58 C140 58 140 63 135 64" fill="none" stroke="var(--gold)" stroke-width="1"/>
    <path d="M126 52 C124 50 128 48 126 46 M130 52 C128 50 132 48 130 46" fill="none" stroke="var(--gold)" stroke-width=".7"/>
  </svg>
  <div class="abs" style="left:90px;top:72px;width:120px;text-align:center;color:#fff">
    <div style="font-size:12.5px;font-weight:500">Section Break</div>
    <div style="font-size:2.8px;margin-top:7px">Take a break and make a cup of coffee</div>
    <div style="font-size:2.8px;margin-top:2px;color:var(--gold)">30 till 45 minutes</div>
  </div>
</section>

<!-- Data table -->
<section class="slide" style="left:325px;top:209px">
  <div class="brand"><i></i>Kalmora</div>
  <h2 class="slide-title">Data Table Concept</h2>
  <svg class="abs" style="left:7px;top:37px" width="65" height="22" viewBox="0 0 65 22">
    <circle cx="11" cy="11" r="10" fill="none" stroke="var(--ink)" stroke-width=".9"/>
    <path d="M7 15 L15 7 M7 7 L15 15" stroke="var(--ink)" stroke-width="1"/>
    <circle cx="41" cy="11" r="10" fill="none" stroke="var(--ink)" stroke-width=".9"/>
    <path d="M41 6 V16 M39 6 H43" stroke="var(--green)" stroke-width="1.2"/>
  </svg>
  <div class="abs" style="left:69px;top:38px;font-size:4.6px;color:var(--gold)">Company budget files 2019</div>
  <p class="abs" style="left:69px;top:47px;width:132px;font-size:2.6px;line-height:1.45;color:#888;font-style:italic">Lorem ipsum dolor sit amet, ligula suspendisse nulla pretium, rhoncus tempor fermentum, enim integer ad vestibulum volutpat. Nisl rhoncus turpis est, vel elit, congue wisi enim nunc ultricies sit, magna tincidunt.</p>
  <table class="table">
    <tr><th style="width:63px">Nisl rhoncus turpis est</th><th>2014</th><th>2015</th><th>2016</th><th>2017</th></tr>
    <tr><td>Praesent condimentum arcu</td><td>4.456</td><td>4.456</td><td>4.456</td><td>4.456</td></tr>
    <tr><td>Praesent condimentum arcu</td><td>5.345</td><td>5.345</td><td>5.345</td><td>5.345</td></tr>
    <tr><td>Praesent condimentum arcu</td><td>6.567</td><td>6.567</td><td>6.567</td><td>6.567</td></tr>
    <tr><td>Praesent condimentum arcu</td><td>7.678</td><td>7.678</td><td>7.678</td><td>7.678</td></tr>
    <tr><td>Praesent condimentum arcu</td><td>8.789</td><td>8.789</td><td>8.789</td><td>8.789</td></tr>
    <tr class="change"><td colspan="5">CHANGE 20%</td></tr>
  </table>
  <div class="stats">
    <div class="head">STATS MANAGER</div>
    <div class="cell">THIS YEAR<b>17,250</b></div>
    <div class="cell">THIS MONTH<b>3,000</b></div>
    <div class="cell">THIS WEEK<b>450</b></div>
    <div class="cell">TODAY<b>225</b></div>
  </div>
  <div class="footer-url"><i></i>www.kalmora-consulting.example</div>
  <svg class="next-arrow" viewBox="0 0 6 5"><path d="M0 2.5H5M3 .5L5 2.5 3 4.5" stroke="var(--green)" stroke-width=".7" fill="none"/></svg>
</section>

<!-- Data chart -->
<section class="slide" style="left:615px;top:209px">
  <div class="brand"><i></i>Kalmora</div>
  <h2 class="slide-title">Data Chart Concept</h2>
  <p class="abs" style="left:80px;top:28px;width:100px;text-align:center;font-size:3px;line-height:1.3;color:#666">The first law of ecology is that everything is related to everything else.</p>
  <svg class="abs" style="left:0;top:0" width="260" height="146" viewBox="0 0 260 146">
    <g stroke="#e6e6e6" stroke-width=".4">
      <line x1="38" y1="46" x2="38" y2="100"/><line x1="84" y1="46" x2="84" y2="100"/>
      <line x1="130" y1="46" x2="130" y2="100"/><line x1="176" y1="46" x2="176" y2="100"/><line x1="222" y1="46" x2="222" y2="100"/>
    </g>
    <line x1="36" y1="100" x2="222" y2="100" stroke="#ccc" stroke-width=".5"/>
    <g>
      <rect x="49" y="62" width="4.5" height="38" fill="var(--green)"/><rect x="57" y="85" width="4.5" height="15" fill="var(--gold)"/><rect x="65" y="82" width="4.5" height="18" fill="var(--graphite)"/>
      <rect x="95" y="84" width="4.5" height="16" fill="var(--green)"/><rect x="103" y="61" width="4.5" height="39" fill="var(--gold)"/><rect x="111" y="82" width="4.5" height="18" fill="var(--graphite)"/>
      <rect x="141" y="69" width="4.5" height="31" fill="var(--green)"/><rect x="149" y="84" width="4.5" height="16" fill="var(--gold)"/><rect x="157" y="73" width="4.5" height="27" fill="var(--graphite)"/>
      <rect x="187" y="62" width="4.5" height="38" fill="var(--green)"/><rect x="195" y="75" width="4.5" height="25" fill="var(--gold)"/><rect x="203" y="55" width="4.5" height="45" fill="var(--graphite)"/>
    </g>
    <g font-size="2.4" fill="#777" font-family="Roboto,sans-serif" text-anchor="middle" letter-spacing=".3">
      <text x="60" y="104.5">CATEGORY 1</text><text x="106" y="104.5">CATEGORY 2</text><text x="152" y="104.5">CATEGORY 3</text><text x="198" y="104.5">CATEGORY 4</text>
    </g>
  </svg>
  <div class="legend"><span class="g">YOUR TITLE</span><span class="o">SOMETHING</span><span class="d">AWESOME</span></div>
  <div class="footer-url"><i></i>www.kalmora-consulting.example</div>
  <svg class="next-arrow" viewBox="0 0 6 5"><path d="M0 2.5H5M3 .5L5 2.5 3 4.5" stroke="var(--green)" stroke-width=".7" fill="none"/></svg>
</section>

<!-- Number data -->
<section class="slide" style="left:905px;top:209px;background:#f2f2f2">
  <div class="brand"><i></i>Kalmora</div>
  <h2 class="slide-title">Our Number Data</h2>
  <div class="abs" style="left:18px;top:32px;width:94px;height:90px;border-radius:4px;background:linear-gradient(180deg,#8aa86a 0%,#5f7a3e 50%,#3a2e22 100%)" role="img" aria-label="Photograph of a hand watering a young seedling in soil"></div>
  <div class="abs" style="left:86px;top:38px;width:44px;height:80px;border-radius:3px;background:#fff;box-shadow:0 1px 3px rgba(0,0,0,.2);text-align:center">
    <div style="width:8px;height:8px;border-radius:50%;background:var(--green-soft);margin:9px auto 5px"></div>
    <div style="font-size:5px;font-weight:500;color:var(--ink)">Environment</div>
    <p style="font-size:2.7px;line-height:1.45;color:#444;margin:3px 5px 0">A wonderful serenity has taken possession of my entire soul,</p>
    <div style="margin:8px auto 0;width:20px;height:6px;border-radius:3px;background:var(--gold);color:#fff;font-size:2.6px;line-height:6px;font-weight:500">Next Slides</div>
  </div>
  <div class="num" style="left:155px;background:var(--green-soft)"><strong>2.152</strong><small>People</small></div>
  <div class="num" style="left:184px;background:var(--gold)"><strong>253</strong><small>Product</small></div>
  <div class="num" style="left:213px;background:#8f8f8f"><strong>4.01K</strong><small>Income</small></div>
  <div class="abs" style="left:155px;top:65px;font-size:5px;color:var(--gold)">About Environment</div>
  <p class="abs" style="left:155px;top:75px;width:88px;font-size:2.7px;line-height:1.5;color:#444;text-align:justify">A wonderful serenity has taken possession of my entire soul, like these sweet mornings of spring which I enjoy with my whole heart. I am alone, and feel the charm of existence in this spot, which was created for the bliss</p>
  <p class="abs" style="left:155px;top:98px;width:88px;font-size:2.7px;line-height:1.5;color:#444;text-align:justify">of souls like mine. I am so happy, my dear friend, so absorbed in the exquisite sense of mere tranquil</p>
  <div class="abs" style="left:155px;top:116px;display:flex;align-items:center;gap:4px;font-size:2.8px;color:#333"><span style="display:block;width:5px;height:3.5px;background:var(--green-soft)"></span>contact@kalmora.example</div>
  <div class="footer-url"><i></i>www.kalmora-consulting.example</div>
  <svg class="next-arrow" viewBox="0 0 6 5"><path d="M0 2.5H5M3 .5L5 2.5 3 4.5" stroke="var(--green)" stroke-width=".7" fill="none"/></svg>
</section>

</body>
</html>
```